Loom, the story of a cursed lawyer (Mira) fighting an almighty Corporation

Pitch : In the aftermath of the terrible atomic attacks that devastated Israel, Washington and Moscow, a new global and almighty Consortium is created, Sarrik. Under the pretext of eradicating nuclear energy, Sarrik has put its hands on all energy sources on the planet. The Allied Assembly has granted it extraordinary rights. Every year, a « Game" is organized in international waters to transform a piece of rock into habitable and energetically autonomous island . The ' Game ' is supposed to promote renewable energies on a global scale. It is in fact the instrument of a gigantic manipulation. Mira, a fallen lawyer, is one of the participants. Aided by an invisible hand, she will discover unspeakable secrets and face an apparently invincible enemy....

science fiction readers

Serif

• Antarctica, Virtual reality, Vimana
• see universe of Teodor Vasquin, Ruben Okafor, or pictures of Orvi

```html
<!DOCTYPE html>
<html lang="fr">
<head>
<meta charset="utf-8">
<title>Loom — Lucien Dormael</title>
<link rel="stylesheet" href="https://fonts.googleapis.com/css2?family=Oswald:wght@400;500&family=Jost:wght@400&family=EB+Garamond:ital,wght@1,500&display=swap">
<style>
  :root {
    --sky-top: #3c5868;
    --sky-mid: #6d8795;
    --haze: #9aa8ae;
    --rock-light: #4a4a4a;
    --rock-dark: #262626;
    --peak: #b08a45;
    --title: #f3f3f3;
    --label: #141414;
    --author: #f5f5f5;
  }
  html, body {
    margin: 0;
    padding: 0;
    width: 800px;
    height: 1200px;
    overflow: hidden;
    background: #1e1e1e;
  }
  .cover {
    position: relative;
    width: 800px;
    height: 1200px;
    overflow: hidden;
  }
  .cover-art {
    position: absolute;
    inset: 0;
    background:
      radial-gradient(ellipse 120px 140px at 365px 340px, rgba(176,138,69,0.55), rgba(176,138,69,0) 100%),
      linear-gradient(to bottom,
        var(--sky-top) 0%,
        var(--sky-mid) 22%,
        var(--haze) 35%,
        var(--rock-light) 40%,
        #3a3a3a 65%,
        var(--rock-dark) 100%);
  }
  .title {
    position: absolute;
    left: 0;
    right: 0;
    top: 520px;
    margin: 0;
    text-align: center;
    font-family: "Oswald", sans-serif;
    font-weight: 400;
    font-size: 290px;
    line-height: 1;
    letter-spacing: 0.14em;
    padding-left: 0.14em;
    color: var(--title);
  }
  .genre {
    position: absolute;
    left: 0;
    right: 0;
    top: 842px;
    margin: 0;
    text-align: center;
    font-family: "EB Garamond", serif;
    font-style: italic;
    font-weight: 500;
    font-size: 25px;
    letter-spacing: 0.03em;
    color: var(--label);
  }
  .author {
    position: absolute;
    left: 0;
    right: 0;
    top: 1098px;
    margin: 0;
    text-align: center;
    font-family: "Jost", sans-serif;
    font-weight: 400;
    font-size: 64px;
    line-height: 1;
    letter-spacing: 0.06em;
    color: var(--author);
  }
</style>
</head>
<body>
  <main class="cover">
    <div class="cover-art" role="img" aria-label="Stormy blue sky above a golden sunlit rocky peak rising out of dark, cracked slate rock"></div>
    <h1 class="title">LOOM</h1>
    <p class="genre">ROMAN</p>
    <p class="author">LUCIEN DORMAEL</p>
  </main>
</body>
</html>
```